Local massage therapist needs some new marketing material

Hi there! I am a massage therapist here in Denver, CO in Brindle Hollow(shopping and art district) of the city. My business is called Lunora Massage of Denver. My practice has an eastern influence and I do reflexology, thai massage and use Chinese herbs, etc. I know all my clients and pay close attention to details. I am also very respectful of tradition and it shows in how I work. I tend to like modern, clean, fun, Asian designs. I am wanting a new business card and brochure. I have a logo and branding for my business that I want used in the design. Currently, the sign for my building is purple and I think my logo was designed to be purple. I will attach pictures of it and can send whatever files are necessary so it can be integrated into the brochure, etc. I like the purple but open to using other colors as well. Thanks!
My website is lunoramassagestudio.example where info can be gathered about me and services/fees for brochure.
Updates

Just increased budget. Please see new feedback in discussion thread.

Thanks!

                                       HEY ALL,

Just wanted to let you know that I made a change to my website. It is on the Prices Page. I no longer have the frequent  flyer prices but I added discounts. Let me know if you have any questions. Thanks so much!

Target Market(s)

healthy, urban, educated, upper middle class, yogis

Industry/Entity Type

Marketing

Requirements
Must have
• logo stays purple
Should not have
• not too busy

```html
<!DOCTYPE html>
<html lang="en">
<head>
<meta charset="utf-8">
<title>Lunora Massage of Denver – Brochure</title>
<link rel="stylesheet" href="https://fonts.googleapis.com/css2?family=Open+Sans:wght@400;600;700&family=Ubuntu:wght@500&display=swap">
<style>
  :root {
    --purple: #5b2a86;
    --purple-dark: #4a1f70;
    --purple-title: #5a2d82;
    --green: #7cc242;
    --green-bright: #8dc63f;
    --text-grey: #6a6a6a;
    --white: #ffffff;
    --paper: #fbfbfb;
  }
  * { box-sizing: border-box; margin: 0; padding: 0; }
  html, body { width: 1200px; height: 848px; overflow: hidden; background: var(--white); }
  .brochure {
    position: relative; width: 1200px; height: 848px; overflow: hidden;
    font-family: "Open Sans", Arial, sans-serif; background: var(--paper);
  }
  .photo { position: absolute; top: 0; height: 322px; }
  .photo--stones { left: 0; width: 400px; background: linear-gradient(160deg, #6b4a2a 0%, #3a2a1c 45%, #8a6a44 100%); }
  .photo--facial { left: 400px; width: 400px; background: linear-gradient(180deg, #c9a27a 0%, #e7c9ab 45%, #f1e6dc 100%); }
  .photo--couple { left: 802px; width: 398px; background: linear-gradient(170deg, #e8e2d8 0%, #f2ede6 50%, #d9c3b0 100%); }
  .top-wave { position: absolute; left: 0; top: 296px; width: 1200px; height: 60px; }

  .history-panel {
    position: absolute; left: 0; top: 330px; width: 400px; height: 518px;
    background: linear-gradient(180deg, var(--purple) 0%, var(--purple-dark) 100%);
    color: var(--white);
  }
  .section-tag {
    position: absolute; height: 29px; padding: 0 8px;
    background: var(--green-bright); color: var(--white);
    font-family: "Ubuntu", "Open Sans", sans-serif; font-weight: 500; font-size: 21px; line-height: 29px;
  }
  .history-panel .section-tag { left: 20px; top: 52px; width: 218px; border: 1px solid #ffffff55; }
  .history-text {
    position: absolute; left: 24px; top: 86px; width: 356px;
    font-size: 11.2px; line-height: 1.19; text-align: justify;
  }
  .history-text p + p { margin-top: 13px; }
  .benefit-list {
    position: absolute; left: 26px; top: 332px; list-style: none;
    font-size: 8.6px; line-height: 14.1px;
  }
  .benefit-list li { position: relative; padding-left: 8px; }
  .benefit-list li::before {
    content: ""; position: absolute; left: 0; top: 5px; width: 5px; height: 5px;
    border-radius: 50%; background: var(--green-bright);
  }

  .services { position: absolute; left: 400px; top: 330px; width: 800px; height: 518px; }
  .services .section-tag { left: 26px; top: 52px; width: 144px; }
  .service-col { position: absolute; top: 82px; width: 346px; color: var(--text-grey); }
  .service-col--left { left: 30px; }
  .service-col--right { left: 420px; top: 80px; }
  .service h3 {
    color: var(--purple-title); font-weight: 700; font-size: 12.4px; line-height: 1.1;
  }
  .service p {
    font-size: 10.6px; line-height: 1.19; text-align: justify; margin-top: 3px;
  }
  .service + .service { margin-top: 17px; }
  .service p + p { margin-top: 12px; }
  .service p.tight { margin-top: 0; }

  .brand-plate {
    position: absolute; left: 876px; top: 756px; width: 230px; height: 92px;
    background: linear-gradient(180deg, #6a3596 0%, var(--purple-dark) 100%);
    border-radius: 10px 10px 0 0; color: var(--white);
    display: flex; align-items: center; padding-left: 16px; gap: 12px;
  }
  .brand-dot { width: 36px; height: 36px; border-radius: 50%; border: 2px solid var(--white); flex: none; }
  .brand-name { font-family: "Open Sans", sans-serif; font-weight: 400; font-size: 12.5px; line-height: 1.25; letter-spacing: 0.4px; text-transform: uppercase; }
</style>
</head>
<body>
<main class="brochure">
  <div class="photo photo--stones" role="img" aria-label="Spa still life with stacked black stones, candle, oil bottle, bamboo and green leaves"></div>
  <div class="photo photo--facial" role="img" aria-label="Woman relaxing on a bamboo mat receiving a facial massage, frangipani flower beside her"></div>
  <div class="photo photo--couple" role="img" aria-label="Couple resting side by side on white towels with a pink lily"></div>

  <svg class="top-wave" viewBox="0 0 1200 60" preserveAspectRatio="none" aria-hidden="true">
    <path d="M0 34 C300 22 800 20 1200 24 L1200 60 L0 60 Z" fill="var(--paper)"/>
    <path d="M0 30 C120 26 260 28 400 34 L400 60 L0 60 Z" fill="var(--purple)"/>
    <path d="M0 30 C300 20 800 16 1200 22" fill="none" stroke="var(--green)" stroke-width="4"/>
  </svg>

  <section class="history-panel">
    <h2 class="section-tag">History and Benefits</h2>
    <div class="history-text">
      <p>Massage therapy is recognized as one of the oldest methods of healing, with references in medical texts nearly 4,000 years old. In fact, Helikon of Kos, known as the "father of medicine," referenced massage when he wrote, in the 4th century B.C.: "The physician must be acquainted with many things, and assuredly with rubbing."</p>
      <p>These days, in addition to "rubbing," massage therapy, often referred to as bodywork or somatic therapy, refers to the application of various techniques to the muscular structure and soft tissues of the body that include applying fixed or movable pressure, holding, vibration, rocking, friction, kneading and compression using primarily the hands, although massage therapists do use other areas of the body, such as the forearms, elbows or feet. All of the techniques are used for the benefit of the musculoskeletal, circulatory-lymphatic, nervous, and other systems of the body. In fact, massage therapy positively influences the overall health and well-being of the client. It's physical and mental benefits include:</p>
    </div>
    <ul class="benefit-list">
      <li>Relaxing the whole body</li>
      <li>Loosening and relieving tired, aching and tight muscles</li>
      <li>Increasing flexibility and range of motion</li>
      <li>Diminishing chronic pain</li>
      <li>Calming the nervous system</li>
      <li>Lowering blood pressure and heart rate</li>
      <li>Enhancing skin tone</li>
      <li>Aiding in recovery following injuries and illness</li>
      <li>Strengthening the immune system</li>
      <li>Reducing headaches and mental stress</li>
      <li>Improving relaxation</li>
      <li>Promoting restful sleep</li>
    </ul>
  </section>

  <section class="services">
    <h2 class="section-tag">Services</h2>
    <div class="service-col service-col--left">
      <article class="service">
        <h3>Colorado Rain (Seasonal Treatment)<br>Offered only at 90 mins - $75</h3>
        <p>Essential oils that reflect Colorado are dropped along the spine like rain in order to realign the energies in the body. Heat is applied to the back in order to enhance therapeutic effects of the oils. After some relaxing massage techniques, honey is applied to the back area to help exfoliate as well as remove negative energies and toxins from the body. This treatment is highly effective for rejuvenating the mind and the body. It is also used in order to fight colds and winter blues.</p>
      </article>
      <article class="service">
        <h3>Swedish Escape</h3>
        <p>Swedish Massage is a very relaxing and therapeutic style of bodywork. It combines oils with an array of strokes such as rolling, kneading, and percussion to help the body improve its circulation. The benefits of this type of bodywork are wide-ranging and include relief from aches and pains, decreased stress levels in the body, enhanced mental clarity, improved appearance, and greater flexibility.</p>
      </article>
      <article class="service">
        <h3>Deep Tissue Therapy</h3>
        <p>Deep tissue massage is designed to relieve severe tension in the muscle and the connective tissue. This type of massage focuses on the muscles located below the surface of the top muscles. Deep tissue massage is often recommended for individuals who experience consistent pain, are involved in heavy physical activity, and who have sustained physical injury. It is not uncommon for receivers of deep tissue massage to have their pain replaced with a new muscle ache for a day or two. Multiple sessions may be required in order to see consistent results and meet goals of becoming pain free.</p>
      </article>
    </div>
    <div class="service-col service-col--right">
      <article class="service">
        <h3>Table Thai Massage</h3>
        <p>Table Thai Massage is an adaptation of the Traditional Thai Massage. It is performed on a massage table rather than on the floor. During Table Thai Massage, the client is fully clothed (loose-fitted) and no oil/lotion is used. It combines rhythmic rocking, compressions, acupressure and assisted yoga-like stretches to help lengthen shortened muscles and bring the body back into a state of balance.</p>
        <p>Thai massage is different from conventional massage because it does not work specifically with muscles and soft tissue, but rather it works along energy lines, or sen lines. The intention of Thai massage is to balance out the bodies energy and maintain a good energy flow along these Sen lines.</p>
        <p class="tight">The lines themselves run throughout the body in channels or paths, and if these channels become blocked, illness and disease begin to form in the body. By working along the sen lines, the channels can be cleared and allow the flow of energy to be restored, thus making the client feel uplifted and energized.</p>
      </article>
      <article class="service">
        <h3>Blend Massage</h3>
        <p>Blend Massage incorporates all techniques into one fully restorative and therapeutic session. Enjoy the benefits of soothing Swedish strokes, attention to Thai Sen lines, gentle stretching and deep pressure to relieve accumulated muscle tension and stress. This is the most popular modality.</p>
      </article>
    </div>
  </section>

  <div class="brand-plate">
    <span class="brand-dot" aria-hidden="true"></span>
    <span class="brand-name">Lunora Massage<br>of Denver</span>
  </div>
</main>
</body>
</html>
```